Brimvale Solutions Website Project

We require a design to revamp and existing website for a company that provides online solutions for small the medium sized businesses including web development, online marketing, social media, online business plans, social media and e-commerce. We are looking to use colours that integrate well with the current logo. Our target market are small to medium sized businesses and individuals looking for a trusted adviser to cover all their online services.
Existing website - www.brimvalesolutions.com.au
Updates
Participation payments added.
Storyboard layout mentioned in brief was not attached in error. It will be uploaded shortly.
Storyboard file added.
Target Market(s)
Revamp of existing website - Looking for a professional design in line with the target market of small to medium businesses
Industry/Entity Type
Business
Requirements
Must have
- Refer the attached storyboard layout for the site design and requirements. Basic header, footer and sidebar are to be the same on every page with the content changing to match the requirements on each page. 8 pages in total
Should not have
- No click here text

```html
<!DOCTYPE html>
<html lang="en">
<head>
<meta charset="utf-8">
<title>Brimvale Solutions</title>
<link href="https://fonts.googleapis.com/css2?family=Signika:wght@400&family=Source+Sans+3:ital,wght@0,400;0,600;1,400&display=swap" rel="stylesheet">
<style>
:root{
  --green:#22b02a;
  --ink:#222;
  --text:#2a2a2a;
  --muted:#777;
  --line:#c8c8c8;
  --panel:#f3f3f3;
  --footer-top:#2c2c2c;
  --footer-bottom:#1b1b1b;
  --base:#0b0b0b;
  --white:#fff;
}
*{margin:0;padding:0;box-sizing:border-box}
html,body{width:1200px;height:1075px;overflow:hidden;background:var(--white)}
body{position:relative;font-family:"Source Sans 3",sans-serif;color:var(--text)}
.top-strip{position:absolute;left:0;top:0;width:1200px;height:7px;background:#dcdcdc}
.header{position:absolute;left:0;top:7px;width:1200px;height:177px;background:linear-gradient(#fff,#f0f0f0);border-bottom:1px solid var(--line)}
.brand{position:absolute;left:36px;top:40px;display:flex;align-items:center;gap:12px}
.brand-dot{width:52px;height:52px;border-radius:50%;background:var(--green)}
.brand-name{font-family:"Signika",sans-serif;font-size:25px;color:var(--ink);line-height:1}
.contact-line{position:absolute;right:42px;top:22px;font-family:"Signika",sans-serif;font-size:19px;color:var(--ink)}
.contact-line .email{font-size:17px}
.social-top{position:absolute;left:1039px;top:61px;display:flex;gap:4px}
.social-dot{width:38px;height:38px;border-radius:50%;background:radial-gradient(circle at 40% 35%,#fff,#cfcfcf);border:1px solid #bbb}
.nav{position:absolute;left:586px;top:119px;height:58px;display:flex;border:1px solid var(--line);border-bottom:none;border-radius:3px 3px 0 0;background:linear-gradient(#fafafa,#e9e9e9)}
.nav a{display:flex;align-items:center;justify-content:center;font-family:"Signika",sans-serif;font-size:18px;color:var(--ink);text-decoration:none;border-left:1px solid var(--line)}
.nav a:first-child{border-left:none}
.content{position:absolute;left:0;top:184px;width:846px;height:586px;background:var(--white);border:1px solid #ddd}
.content h1{position:absolute;left:27px;top:24px;width:783px;font-family:"Signika",sans-serif;font-weight:400;font-size:22px;color:var(--ink);padding-bottom:10px;border-bottom:1px solid #aaa}
.content .copy{position:absolute;left:27px;top:78px;width:792px;font-size:14.4px;line-height:24px;color:var(--text)}
.copy p+p{margin-top:24px}
.copy p.tight{margin-top:0}
.sidebar{position:absolute;left:846px;top:184px;width:354px;height:594px;background:var(--panel)}
.sidebar-head{height:58px;background:linear-gradient(#f7f7f7,#e4e4e4);border-bottom:1px solid var(--line);font-family:"Signika",sans-serif;font-size:23px;color:var(--ink);padding:17px 0 0 30px}
.field-label{position:absolute;left:22px;font-family:"Signika",sans-serif;font-size:16.5px;color:var(--ink)}
.field{position:absolute;left:18px;width:314px;height:37px;background:var(--white);border:1px solid #d6d6d6;border-radius:4px;font-style:italic;font-size:14px;color:var(--muted);padding:9px 12px;box-shadow:0 4px 6px -3px rgba(0,0,0,.15)}
.field.area{height:137px}
.submit{position:absolute;left:22px;top:531px;width:114px;height:35px;border-radius:3px;background:var(--green);color:var(--white);font-family:"Signika",sans-serif;font-size:16px;display:flex;align-items:center;justify-content:center}
.footer{position:absolute;left:0;top:778px;width:1200px;height:249px;background:linear-gradient(var(--footer-top),var(--footer-bottom));color:#ddd}
.footer h2{position:absolute;font-family:"Signika",sans-serif;font-weight:400;font-size:18px;color:var(--white)}
.links{position:absolute;top:65px;list-style:none;font-size:13.5px;line-height:27.6px;color:#ddd}
.blog-text{position:absolute;left:581px;top:64px;width:360px;font-style:italic;font-size:13.5px;line-height:21.6px;color:#ddd}
.author{position:absolute;left:581px;top:165px;width:145px;height:31px;background:#0a0a0a;border-radius:3px;color:var(--white);font-size:15px;display:flex;align-items:center;justify-content:center}
.social-foot{position:absolute;left:991px;top:65px;display:flex;gap:4px}
.base{position:absolute;left:0;top:1027px;width:1200px;height:48px;background:var(--base);border-top:2px solid #333;color:#ddd;font-size:13.5px;padding:16px 0 0 28px}
</style>
</head>
<body>
<div class="top-strip"></div>
<header class="header">
  <div class="brand"><span class="brand-dot"></span><span class="brand-name">Brimvale Solutions</span></div>
  <div class="contact-line">265 555 0148 &nbsp;|&nbsp; <span class="email">hello@brimvale.example</span></div>
  <div class="social-top"><span class="social-dot"></span><span class="social-dot"></span><span class="social-dot"></span></div>
  <nav class="nav">
    <a style="width:98px">Home</a><a style="width:106px">About Us</a><a style="width:96px">Services</a><a style="width:108px">Portfolio</a><a style="width:70px">Blog</a><a style="width:106px">Contact</a>
  </nav>
</header>

<main class="content">
  <h1>About Our Business</h1>
  <div class="copy">
    <p>Larkfield eSolutions is a professional website design company dedicated to provide excellent services. We at Larkfield eSolutions think graphic design as a combination and collaboration of ideas and technology. Our Website Design team give an unforgettable impression on the customers and the clients. We can assure you that this is the best place for requirement of yours regarding website design solutions</p>
    <p>Larkfield eSolutions provides you the Search Engine Optimization making your website search engine friendly. So that the website can achieve top position and ranking in the Internet searches and thereby increasing the scope for the website to be found by customers. We here modify the site to improve the ranking by using the keywords and contents.</p>
    <p>E-Commerce is a major progress in technology that has changed the way in which the customers now purchase information, products and the services. It’s the new way of providing an opportunity to make your products and services available in the global market 24 hours a day through Internet</p>
    <p class="tight">Larkfield eSolutions is specialized in handling advanced web projects and the ongoing projects that require permanent maintenance and support .We like challenges and do complete these challenge with expertise we like solving questions that arises in such projects as these helps us to grow also. The only way to success is through the right path and that’s what we provide you. None of the other companies has the result we do. So stick to the best that’s how you will be the best don’t opt for the second best. Our expertise does not limit itself to web development but also it includes Web Hosting, Search Engine Optimization, E-Commerce. We partner hundreds of organization to enhance their business, marketing and profit goals.</p>
  </div>
</main>

<aside class="sidebar">
  <div class="sidebar-head">Quick Quote</div>
  <div class="field-label" style="top:92px">Full Name</div>
  <div class="field" style="top:109px">type your name</div>
  <div class="field-label" style="top:180px">Email address</div>
  <div class="field" style="top:195px">type your email address</div>
  <div class="field-label" style="top:264px">Phone no.</div>
  <div class="field" style="top:279px">type your phone no.</div>
  <div class="field-label" style="top:354px">Message</div>
  <div class="field area" style="top:372px">message</div>
  <div class="submit">Submit Now</div>
</aside>

<footer class="footer">
  <h2 style="left:41px;top:30px">Quick Links</h2>
  <ul class="links" style="left:41px"><li>Home Page</li><li>About Us</li><li>Services</li><li>Portfolio</li></ul>
  <ul class="links" style="left:156px"><li>E-Commerce</li><li>Web Development</li><li>Recent Blog</li><li>Quick Quote</li></ul>
  <ul class="links" style="left:315px"><li>Marketing</li><li>Business</li><li>Social Media</li></ul>
  <ul class="links" style="left:438px;line-height:30px"><li>FAQ</li><li>Support</li><li>Contact</li></ul>
  <h2 style="left:581px;top:30px">Last Blog Post</h2>
  <p class="blog-text">Our Website Design team give an unforgettable impression on the customers and the clients. We can assure you that this is the best place for requirement of yours regarding website design solutions</p>
  <div class="author">BY Author Name</div>
  <h2 style="left:989px;top:31px">Social Media</h2>
  <div class="social-foot"><span class="social-dot"></span><span class="social-dot"></span><span class="social-dot"></span></div>
</footer>
<div class="base">© 2012 Company Name &nbsp;|&nbsp; All right reserved</div>
</body>
</html>
```